Flier for digital rights event targetting TMVA trade negotiators

We need a design for an event that my organization (a nonprofit) is hosting with academic experts, to address government negotiators who are taking part in the 19th round of negotiations of the Coastal Integrated Commerce Accord (TMVA). Unfortunately we don't have the exact details yet such as who the speakers are, what date the meeting is, or even what location it is, other than that it will be in Hyderabad, India. So you will need to make a design with placeholder values that we can swap out later. Here is some information about TMVA: https://en.examplepedia.org/wiki/Coastal_Integrated_Commerce_Accord. The event will be called: "An Expert Roundtable on Electronic Commerce and TMVA". I'm attaching some similar fliers for previous events.

Target Market(s)

Government trade ministries

Industry/Entity Type

Trade

Font styles to use
Serif
Sans Serif

Colors

Designer to choose colors to be used in the design.

Requirements
Must have
• Space for organizer logos, including LKB logo from https://www.lkbnet.org/press/logos
Nice to have
• Space for headshots of speakers (even though we haven't finalized who they are yet)
Should not have
• Cheesy stock graphics

```html
<!DOCTYPE html>
<html lang="en">
<head>
<meta charset="utf-8">
<title>An Expert Roundtable on Electronic Commerce and TMVA</title>
<link href="https://fonts.googleapis.com/css2?family=Lato:ital,wght@0,300;0,400;0,700;1,400;1,700;1,900&display=swap" rel="stylesheet">
<style>
  :root {
    --page-bg: #a8a5a1;
    --banner-top: #f7f7f7;
    --banner-mid: #eeeeee;
    --banner-edge: #d9d9d9;
    --banner-frame: #5b6261;
    --title-green: #1c3226;
    --ink: #1b1b1b;
    --photo-light: #c9c9c9;
    --photo-dark: #4a4a4a;
    --photo-frame: #2a2a2a;
    --table-light: #5c6665;
    --table-dark: #3d4645;
    --scene-bg: #e6e6e6;
    --accent-red: #d9302a;
  }
  * { margin: 0; padding: 0; box-sizing: border-box; }
  html, body { width: 1200px; height: 1000px; overflow: hidden; }
  body {
    background: var(--page-bg);
    font-family: "Lato", Arial, sans-serif;
    position: relative;
  }
  .banner {
    position: absolute;
    left: 100px; top: 312px;
    width: 992px; height: 380px;
    border: 2px solid var(--banner-frame);
    background: radial-gradient(ellipse at 45% 55%, var(--banner-top) 0%, var(--banner-mid) 60%, var(--banner-edge) 100%);
    overflow: hidden;
  }
  .title {
    position: absolute;
    left: 26px; top: 14px;
    font-weight: 700;
    font-size: 58px;
    line-height: 1;
    color: var(--title-green);
    letter-spacing: -0.3px;
  }
  .subtitle {
    position: absolute;
    left: 28px; top: 76px;
    font-weight: 300;
    font-size: 31px;
    line-height: 1;
    color: var(--title-green);
  }
  .accord-name {
    position: absolute;
    left: 30px; top: 112px;
    font-weight: 700;
    font-style: italic;
    font-size: 19px;
    color: var(--title-green);
  }
  .speaker {
    position: absolute;
    top: 153px;
    width: 106px;
    text-align: center;
  }
  .speaker--first { left: 29px; }
  .speaker--second { left: 154px; }
  .speaker-photo {
    width: 106px; height: 131px;
    border: 1px solid var(--photo-frame);
    background: linear-gradient(160deg, var(--photo-light) 0%, #8e8e8e 55%, var(--photo-dark) 100%);
    box-shadow: 2px 3px 6px rgba(0,0,0,0.35);
  }
  .speaker-name {
    margin-top: 10px;
    font-style: italic;
    font-size: 15px;
    color: var(--ink);
    white-space: nowrap;
    margin-left: -20px; margin-right: -20px;
  }
  .organizer {
    position: absolute;
    left: 28px; top: 326px;
    display: flex;
    flex-direction: column;
    align-items: center;
    gap: 3px;
  }
  .organizer-mark {
    display: flex; align-items: center; gap: 4px;
    font-weight: 700; font-size: 16px; color: var(--ink);
  }
  .organizer-dot {
    width: 14px; height: 14px; border-radius: 50%;
    background: var(--accent-red);
  }
  .organizer-name {
    font-weight: 700; font-size: 5.5px; letter-spacing: 0.3px;
    color: var(--ink); text-transform: uppercase;
  }
  .details {
    position: absolute;
    left: 303px; top: 152px;
    font-size: 15px;
    color: var(--ink);
    line-height: 20px;
  }
  .details-label {
    font-weight: 900;
    font-style: italic;
    font-size: 16px;
  }
  .details-label--rsvp { margin-top: 16px; }
  .meeting-scene {
    position: absolute;
    left: 640px; top: 18px;
    width: 350px; height: 350px;
    border-radius: 50%;
    background: radial-gradient(circle, var(--table-light) 0%, var(--table-dark) 62%, var(--scene-bg) 78%, transparent 80%);
  }
</style>
</head>
<body>
  <section class="banner">
    <h1 class="title">An Expert Roundtable</h1>
    <p class="subtitle">on Electronic Commerce and TMVA</p>
    <p class="accord-name">Coastal Integrated Commerce Accord</p>

    <figure class="speaker speaker--first">
      <div class="speaker-photo" role="img" aria-label="Black and white headshot of speaker Daniel Ferris"></div>
      <figcaption class="speaker-name">Daniel Ferris</figcaption>
    </figure>
    <figure class="speaker speaker--second">
      <div class="speaker-photo" role="img" aria-label="Black and white headshot of speaker Harold Kessler"></div>
      <figcaption class="speaker-name">Harold Kessler</figcaption>
    </figure>

    <div class="organizer">
      <div class="organizer-mark"><span class="organizer-dot"></span>LKB</div>
      <div class="organizer-name">Lantern Knowledge Bureau</div>
    </div>

    <div class="details">
      <div class="details-label">Date and Place:</div>
      <div>01 06 2017&nbsp; | &nbsp;Hyderabad, India</div>
      <div class="details-label">Venue:</div>
      <div class="details-label details-label--rsvp">RSVP:</div>
    </div>

    <div class="meeting-scene" role="img" aria-label="Top-down illustration of negotiators seated around a round table with laptops and papers"></div>
  </section>
</body>
</html>
```